LoweniasMassage website required

We need a website for a mobile sports massage therapist in the United Kingdom. Specialising in pregnancy and postnatal massage, sports and remedial, deep tissue massage & Corprate Massage. Attached are some logos that we already have in various colours. The file named logo_white_background is what we normally use. Feel free to use the others at your discretion.

Requirements
Must have
• Service areas, Booking system.

```html
<!DOCTYPE html>
<html lang="en">
<head>
<meta charset="utf-8">
<title>LoweniasMassage</title>
<link rel="stylesheet" href="https://fonts.googleapis.com/css2?family=Montserrat:wght@400;500;600;700&family=Questrial&display=swap">
<style>
:root{
  --ink:#2b2b2b;
  --muted:#5a5a5a;
  --accent:#ffc60b;
  --sky:#6aa8ea;
  --sky-band:#8cc3f8;
  --rule:#b9d6f2;
  --footer:#3d3d3d;
  --paper:#ffffff;
}
*{box-sizing:border-box;margin:0;padding:0}
html,body{width:1200px;height:3396px;overflow:hidden;background:var(--paper)}
body{position:relative;font-family:"Questrial",sans-serif;color:var(--ink)}
.abs{position:absolute}

/* hero */
.hero{left:0;top:0;width:1200px;height:611px;
  background:linear-gradient(115deg,#2f5fd0 0%,#6f93d8 30%,#c9d6ec 55%,#eef2f8 75%,#f7f8fb 100%)}
.brand{left:50px;top:62px;font-family:"Montserrat",sans-serif;font-weight:600;font-size:19px;color:var(--ink)}
.nav{top:100px;right:34px;display:flex;gap:70px;font-family:"Montserrat",sans-serif;font-size:13px;font-weight:600;letter-spacing:2px;color:var(--ink)}
.hero-title{left:95px;top:370px;font-family:"Montserrat",sans-serif;font-weight:500;font-size:45px;line-height:50px;color:#fff}
.btn{display:flex;align-items:center;justify-content:center;gap:12px;background:var(--accent);color:#fff;
  font-family:"Montserrat",sans-serif;font-size:12px;font-weight:600;letter-spacing:3px}
.hero-btn{left:163px;top:482px;width:177px;height:34px}

/* section headings */
.heading{left:0;width:1200px;text-align:center;font-family:"Montserrat",sans-serif}
.offer-title{top:796px;font-size:44px;font-weight:600;letter-spacing:9px}
.pricing-title{top:1268px;font-size:44px;font-weight:400;letter-spacing:8px}
.rule{height:2px;background:var(--rule)}
.intro{left:200px;width:800px;top:886px;text-align:center;font-size:16px;line-height:22px;color:var(--muted)}

/* offer cards */
.service-photo{top:962px;width:177px;height:215px}
.service-label{top:1109px;width:226px;height:46px;font-size:11px;letter-spacing:1px}

/* pricing */
.price{font-family:"Montserrat",sans-serif}
.price h3{font-size:27px;font-weight:500;letter-spacing:5px;color:var(--sky);line-height:30px}
.price p{font-family:"Questrial",sans-serif;font-size:16px;line-height:25px;color:var(--muted)}

/* why */
.why-photo{left:0;top:1965px;width:591px;height:487px;background:linear-gradient(180deg,#e9e9ea 0%,#c8ccd2 45%,#3d4a66 100%)}
.why-band{left:591px;top:1965px;width:609px;height:487px;background:var(--sky-band)}
.why-title{left:591px;width:609px;top:2127px;text-align:center;font-family:"Montserrat",sans-serif;font-size:28px;letter-spacing:3px;color:#fff}
.why-text{left:646px;width:500px;top:2184px;text-align:center;font-size:14px;line-height:22px;color:#eaf4ff}

/* booking */
.map{left:0;top:2456px;width:1200px;height:442px;background:linear-gradient(135deg,#f3f3f3,#e6e6e6 50%,#f0f0f0)}
.booking-title{left:158px;top:2582px;font-family:"Montserrat",sans-serif;font-weight:600;font-size:22px}
.field{left:158px;width:172px;height:34px;border:1px solid #bdbdbd;background:#fff;display:flex;align-items:center;padding:0 10px;gap:10px;font-size:10px;color:#999}
.booking-btn{top:2760px;width:68px;height:30px;font-size:9px;letter-spacing:1px}
.ghost{background:#fff;color:var(--ink);border:3px solid var(--accent)}
.forgot{left:158px;top:2802px;font-size:9px;color:#444}

/* promo */
.promo-title{top:2968px;font-size:16px;font-weight:600;letter-spacing:4px}
.promo-text{left:390px;width:420px;top:3003px;text-align:center;font-size:10px;line-height:14px;color:var(--muted)}
.promo-btn{left:551px;top:3043px;width:125px;height:23px;font-size:10px}

/* footer */
.footer{left:0;top:3163px;width:1200px;height:233px;background:var(--footer);color:#fff}
.footer h4{font-family:"Montserrat",sans-serif;font-size:19px;font-weight:600}
.footer ul{list-style:none;font-size:10px;line-height:14px;margin-top:10px}
.footer p{font-size:11px;line-height:15px;letter-spacing:1.5px;margin-top:10px;width:420px;color:#ddd}
</style>
</head>
<body>

<div class="abs hero" role="img" aria-label="Therapist stretching a client's leg during a sports massage"></div>
<div class="abs brand">LoweniasMassage</div>
<nav class="abs nav"><span>HOME</span><span>ABOUT</span><span>SERVICES</span><span>BOOKING</span></nav>
<h1 class="abs hero-title">Book now and<br>Get a 20% Discount</h1>
<div class="abs btn hero-btn">Click Here
  <svg width="10" height="12" viewBox="0 0 10 12"><path d="M0 0L10 6L0 12Z" fill="#fff"/></svg></div>

<h2 class="abs heading offer-title">WHAT WE OFFER</h2>
<div class="abs rule" style="left:374px;top:860px;width:436px"></div>
<p class="abs intro">Lorem ipsum dolor sit amet, consectetuer adipiscing elit, sed diam nonummy nibh euismod tincidunt ut laoreet dolore magna aliquam erat volutpat.</p>

<div class="abs service-photo" style="left:222px;background:linear-gradient(180deg,#8bb34a,#d9a07c 60%,#f1d3bd)" role="img" aria-label="Hands forming a heart over a pregnant belly"></div>
<div class="abs service-photo" style="left:514px;background:linear-gradient(180deg,#e7c3a4,#c58c63 60%,#f3e6da)" role="img" aria-label="Client relaxing during a deep tissue massage"></div>
<div class="abs service-photo" style="left:808px;background:linear-gradient(180deg,#6f86a3,#2c2c34 60%,#1c1c20)" role="img" aria-label="Seated shoulder massage in an office"></div>
<div class="abs btn service-label" style="left:195px">Postnatal Massage</div>
<div class="abs btn service-label" style="left:488px">Deep Tissue Massage</div>
<div class="abs btn service-label" style="left:781px">Corporate Massage</div>

<h2 class="abs heading pricing-title">PRICING LIST</h2>
<div class="abs rule" style="left:380px;top:1331px;width:440px"></div>

<div class="abs price" style="left:245px;top:1413px"><h3>Lorem Ipsum</h3><p>Lorem Ipsum - £ 50.00<br>Lorem Ipsum - £ 50.00<br>Lorem Ipsum - £ 50.00</p></div>
<div class="abs price" style="left:715px;top:1413px"><h3>Lorem Ipsum</h3><p>Lorem Ipsum - £ 50.00<br>Lorem Ipsum - £ 50.00<br>Lorem Ipsum - £ 50.00</p></div>
<div class="abs price" style="left:245px;top:1583px"><h3>Lorem Ipsum</h3><p>Lorem Ipsum - £ 50.00<br>Lorem Ipsum - £ 50.00<br>Lorem Ipsum - £ 50.00</p></div>
<div class="abs price" style="left:715px;top:1583px"><h3>Lorem Ipsum</h3><p>Lorem Ipsum - £ 50.00<br>Lorem Ipsum - £ 50.00<br>Lorem Ipsum - £ 50.00</p></div>
<div class="abs price" style="left:245px;top:1778px"><h3>Lorem Ipsum</h3><p>Lorem Ipsum - £ 50.00<br>Lorem Ipsum - £ 50.00<br>Lorem Ipsum - £ 50.00</p></div>
<div class="abs price" style="left:715px;top:1778px"><h3>Lorem Ipsum</h3><p>Lorem Ipsum - £ 50.00<br>Lorem Ipsum - £ 50.00<br>Lorem Ipsum - £ 50.00</p></div>

<div class="abs why-photo" role="img" aria-label="Bright treatment room with a massage table by the window"></div>
<div class="abs why-band"></div>
<h2 class="abs why-title">WHY CHOOSE US</h2>
<div class="abs rule" style="left:763px;top:2168px;width:264px;background:#d9ecff"></div>
<p class="abs why-text">Lorem ipsum dolor sit amet, consectetuer adipiscing elit, sed diam nonummy nibh euismod tincidunt ut laoreet dolore magna aliquam erat volutpat. Ut wisi enim ad minim veniam, quis nostrud exerci tation ullamcorper suscipit lobortis nisl ut aliquip ex ea commodo consequat.</p>

<div class="abs map" role="img" aria-label="Street map of the service area"></div>
<h2 class="abs booking-title">Online Booking</h2>
<div class="abs field" style="top:2614px;justify-content:space-between">Name Service Massage
  <svg width="14" height="9" viewBox="0 0 14 9"><path d="M1 1L7 7L13 1" stroke="#333" stroke-width="2" fill="none"/></svg></div>
<div class="abs field" style="top:2664px">
  <svg width="14" height="14" viewBox="0 0 14 14"><path d="M7 1L13 13H1Z" stroke="#555" stroke-width="1.4" fill="none"/></svg>Username</div>
<div class="abs field" style="top:2712px">
  <svg width="12" height="14" viewBox="0 0 12 14"><rect x="1" y="6" width="10" height="7" rx="1" stroke="#555" stroke-width="1.4" fill="none"/><path d="M3 6V4a3 3 0 0 1 6 0v2" stroke="#555" stroke-width="1.4" fill="none"/></svg>Password</div>
<div class="abs btn booking-btn" style="left:158px">Log In</div>
<div class="abs btn booking-btn ghost" style="left:262px">Log out</div>
<div class="abs forgot">Forgot User ID or Password</div>

<h2 class="abs heading promo-title">GET NOTIFIED FOR MONTHLY PROMOS</h2>
<p class="abs promo-text">Lorem ipsum dolor sit amet, consectetuer adipiscing elit, sed diam nonummy nibh euismod tincidunt ut laoreet dolore magna aliquam erat volutpat.</p>
<div class="abs btn promo-btn">Click Here
  <svg width="7" height="8" viewBox="0 0 10 12"><path d="M0 0L10 6L0 12Z" fill="#fff"/></svg></div>

<footer class="abs footer">
  <div class="abs" style="left:294px;top:62px">
    <h4>Categories</h4>
    <ul><li>- HOME</li><li>- ABOUT</li><li>- SERVICES</li><li>- BOOKINGS</li></ul>
  </div>
  <div class="abs" style="left:602px;top:64px">
    <h4>About Us</h4>
    <p>Lorem ipsum dolor sit amet, consectetuer adipiscing elit, sed diam nonummy nibh euismod tincidunt ut laoreet dolore magna aliquam erat volutpat. Ut wisi enim ad minim veniam, quis nostrud exerci tation ullamcorper suscipit lobortis nisl ut aliquip.</p>
  </div>
</footer>

</body>
</html>
```